Membership Sales Page Web Design

We need a website designed to showcase the benefits of joining our online community of technology procurement professionals.

Our community has been around for a while and it's time for a refresh. Included in the brief is Verson 1.0 of the site. You can see the current version of the site @ brivolnet.com.

As part of the refresh, we've acquired a new primary domain name (brivol.com) and will be rolling out both a free and paid subscription model.

Because of this, there should be a strong call to sign (join now) infused within the site.

We would like to see site designs that are clean, flat and minimalistic in nature. Our membership colors are royal blue, grey, and white.

The final design should communicate networking and professional growth.

I'd be particularly interestedin seeing some flat website designs with a strong call to action. Here are some great examples for inspiration:

https://plintora.example/
https://vemmit.example/

Target Market(s)

zenthar 300 companies

Number of Pages Required

1 page

Font styles to use
Sans Serif

Colors
0293ce
3276b5
ffffff

Requirements
Must have
• clean, minimalistic, fee
strong call to action
showcase our different membership levels
highlight the benefits of membership
Nice to have
• n/a
Should not have
• n/a

```html
<!DOCTYPE html>
<html lang="en">
<head>
<meta charset="utf-8">
<title>BRIVOL – Membership</title>
<link href="https://fonts.googleapis.com/css2?family=Rubik:wght@300;400;500;700&display=swap" rel="stylesheet">
<style>
:root{
  --navy:#232a4a;
  --muted:#8a90a6;
  --blue:#0293ce;
  --page:#f7f8fa;
  --panel:#eef0f5;
  --white:#ffffff;
  --footer:#222b3d;
  --rule:#e3e6ee;
}
*{box-sizing:border-box;margin:0;padding:0}
html,body{width:1200px;height:3098px;overflow:hidden}
body{position:relative;background:var(--page);font-family:'Rubik',sans-serif;color:var(--navy)}
.abs{position:absolute}
.hero-bg{left:0;top:0;width:745px;height:675px;background:var(--white);border-bottom-right-radius:240px}
.logo{left:158px;top:24px;display:flex;align-items:center;gap:8px;font-weight:700;font-size:22px;color:var(--blue);letter-spacing:1px}
.logo-mark{width:12px;height:12px;background:var(--blue)}
.nav a{position:absolute;top:32px;font-size:10.5px;color:var(--muted);text-decoration:none}
.nav a.active{color:var(--navy);font-weight:500}
.nav a.active::after{content:"";position:absolute;left:0;right:0;top:19px;height:2px;background:var(--blue)}
.join-link{left:907px;top:33px;font-size:9px;font-weight:700;color:var(--navy)}
.members-btn{left:975px;top:23px;width:73px;height:32px;border-radius:7px;background:var(--blue);color:var(--white);font-size:9px;font-weight:700;display:flex;align-items:center;justify-content:center}
.hero-title{left:151px;top:218px;font-size:27px;font-weight:700;line-height:49px}
.cta{left:151px;top:374px;width:186px;height:42px;border-radius:7px;background:var(--blue);color:var(--white);font-size:11px;font-weight:700;display:flex;align-items:center;justify-content:center}
.cta-note{left:151px;top:436px;font-size:11px;font-weight:500;color:var(--muted)}
.photo{background:linear-gradient(135deg,#c9ccd3,#8f7a66)}
.dots{background:rgba(200,204,214,.35)}
.accent{background:var(--blue)}
.rule{height:2px;background:var(--blue)}
.sec-title{left:0;width:1200px;text-align:center;font-size:20px;font-weight:700}
.panel{background:var(--panel);border-radius:8px}
.card-title{font-size:15px;font-weight:700}
.para{font-size:11px;font-weight:300;color:var(--muted);line-height:26.3px;white-space:nowrap}
.icon-box{width:33px;height:32px;border-radius:8px;display:flex;align-items:center;justify-content:center}
.benefits{list-style:none}
.benefits li{height:28.9px;display:flex;align-items:center;gap:14px;font-size:11px;font-weight:300;color:var(--muted)}
.plan{background:var(--white);border-radius:8px;box-shadow:0 6px 24px rgba(35,42,74,.04)}
.plan h3{position:absolute;left:38px;top:36px;font-size:15px;font-weight:700}
.price{position:absolute;left:38px;top:74px;font-size:28px;font-weight:700}
.price small{font-size:12px;color:var(--muted);font-weight:500;margin-left:6px}
.plan-sub{position:absolute;left:38px;top:126px;font-size:11px;font-weight:300;color:var(--muted)}
.features{position:absolute;left:38px;top:165px;list-style:none}
.features li{height:35px;display:flex;align-items:center;gap:8px;font-size:11px;font-weight:500}
.plan-btn{position:absolute;left:38px;top:323px;width:217px;height:40px;border-radius:7px;border:1px solid var(--blue);color:var(--blue);font-size:11px;font-weight:700;display:flex;align-items:center;justify-content:center}
.plan-btn.solid{background:var(--blue);color:var(--white)}
.foot-col h4{font-size:10px;font-weight:500;margin-bottom:11px}
.foot-col p{font-size:9.5px;font-weight:300;color:var(--muted);line-height:24px;white-space:nowrap}
.bottom-bar{left:0;top:3046px;width:1200px;height:52px;background:var(--footer);color:var(--white)}
.social{position:absolute;top:20px;font-size:9px;font-weight:400;color:var(--white)}
</style>
</head>
<body>

<div class="abs hero-bg"></div>

<header>
  <div class="abs logo"><span class="logo-mark"></span>BRIVOL</div>
  <nav class="nav">
    <a class="active" style="left:302px">Home</a>
    <a style="left:368px">Featured Events</a>
    <a style="left:485px">Offerings</a>
    <a style="left:568px">Shop</a>
    <a style="left:630px">Certification</a>
  </nav>
  <div class="abs join-link">JOIN NOW</div>
  <div class="abs members-btn">MEMBERS</div>
</header>

<section class="hero">
  <h1 class="abs hero-title">Sharing Experiences,<br>Powerful Tools and<br>Proven Solutions</h1>
  <div class="abs cta">JOIN NOW</div>
  <p class="abs cta-note">Save $600, limited space early-bird expires January 31</p>

  <div class="abs dots" style="left:563px;top:106px;width:75px;height:114px" role="img" aria-label="Dot grid decoration"></div>
  <div class="abs photo" style="left:600px;top:106px;width:216px;height:282px;border-bottom-right-radius:72px;background:linear-gradient(135deg,#d9d6d2,#7d7068)" role="img" aria-label="Team of professionals collaborating around a laptop"></div>
  <div class="abs photo" style="left:832px;top:106px;width:216px;height:144px;border-top-right-radius:60px;background:linear-gradient(135deg,#f1f2f3,#c7ccd0)" role="img" aria-label="Desktop computer on a bright white desk"></div>
  <div class="abs photo" style="left:832px;top:263px;width:216px;height:270px;border-bottom-right-radius:72px;background:linear-gradient(135deg,#6a4a35,#3f2a1e)" role="img" aria-label="Overhead view of a wooden meeting table with laptops"></div>
  <div class="abs accent" style="left:724px;top:402px;width:92px;height:81px;border-top-left-radius:40px;border-bottom-right-radius:40px"></div>
</section>

<section class="about">
  <div class="abs rule" style="left:586px;top:748px;width:29px"></div>
  <h2 class="abs sec-title" style="top:769px">Promoting Excellence Among Acquisition Professionals</h2>

  <div class="abs panel" style="left:151px;top:868px;width:897px;height:292px"></div>
  <div class="abs photo" style="left:170px;top:887px;width:293px;height:254px;border-radius:6px;background:linear-gradient(135deg,#e8c891,#d8b276)" role="img" aria-label="Keyboard, mouse and notebook on a tan desk"></div>
  <h3 class="abs card-title" style="left:506px;top:955px">What is BRIVOL?</h3>
  <p class="abs para" style="left:506px;top:986px">BRIVOL is the only association serving the specialized needs of the technology acquisition<br>professional—the person responsible for negotiating and managing contracts with suppliers of<br>technology products and services.</p>

  <div class="abs panel" style="left:151px;top:1181px;width:293px;height:260px"></div>
  <div class="abs icon-box" style="left:170px;top:1199px;background:#dfe9f5">
    <svg width="12" height="12" viewBox="0 0 12 12" fill="none" stroke="#3276b5" stroke-width="1.2"><path d="M1 9l3.5-3.5 2 2L11 3M8 3h3v3"/></svg>
  </div>
  <h3 class="abs card-title" style="left:214px;top:1206px">What is its mission?</h3>
  <p class="abs para" style="left:170px;top:1245px">The BRIVOL mission is to promote and support<br>excellence and professionalism among<br>technology procurement professionals. Brivol<br>works diligently to increase the effectiveness,<br>the image and the impact of these professionals<br>as they serve their organizations and<br>constituents.</p>

  <div class="abs panel" style="left:454px;top:1181px;width:291px;height:260px"></div>
  <div class="abs icon-box" style="left:473px;top:1199px;background:#dfe9f5">
    <svg width="12" height="12" viewBox="0 0 12 12" fill="none" stroke="#3276b5" stroke-width="1.1"><circle cx="4.5" cy="4" r="2"/><path d="M1 11c0-2 1.5-3.5 3.5-3.5S8 9 8 11M8 2a2 2 0 010 4M9.5 7.8c1 .5 1.5 1.6 1.5 3.2"/></svg>
  </div>
  <h3 class="abs card-title" style="left:516px;top:1206px">Who is BRIVOL?</h3>
  <p class="abs para" style="left:473px;top:1245px">BRIVOL members come from a variety of skill<br>levels and disciplines from all sectors of the<br>economy, including procurement, finance, legal,<br>information technology and contract<br>management. Their organizations vary from<br>single-practitioner shops to large, highly<br>specialized departments.</p>

  <div class="abs panel" style="left:756px;top:1181px;width:292px;height:260px"></div>
  <div class="abs icon-box" style="left:775px;top:1199px;background:#fbf1d9">
    <svg width="13" height="13" viewBox="0 0 12 12" fill="none" stroke="#e9a21a" stroke-width="1"><path d="M6 1l1.5 3.2 3.5.4-2.6 2.4.7 3.5L6 8.8 2.9 10.5l.7-3.5L1 4.6l3.5-.4z"/></svg>
  </div>
  <h3 class="abs card-title" style="left:818px;top:1206px">Why should I join?</h3>
  <p class="abs para" style="left:775px;top:1245px">As a member, you will learn what kind of deals<br>others are doing, share information and<br>experiences, obtain information about vendor<br>ploys and practices, stay informed on best and<br>worst deals, keep up with legislative and<br>regulatory issues affecting your job, and much<br>more.</p>
</section>

<section class="membership">
  <div class="abs rule" style="left:151px;top:1598px;width:29px"></div>
  <h2 class="abs" style="left:151px;top:1619px;font-size:20px;font-weight:700">Become a member today.</h2>
  <p class="abs para" style="left:151px;top:1649px">If you're the person responsible for negotiating and managing<br>contracts with vendors of technology products and services,<br>BRIVOL membership is for you. It will enhance your<br>performance and facilitate your professional growth while you<br>network with others to advance the art and science of<br>technology procurement.</p>
  <ul class="abs benefits" style="left:151px;top:1822px">
    <li><svg width="13" height="13" viewBox="0 0 14 14"><circle cx="7" cy="7" r="7" fill="#232a4a"/><path d="M4 7.2l2 2 4-4" stroke="#fff" stroke-width="1.5" fill="none"/></svg>Work Smart</li>
    <li><svg width="13" height="13" viewBox="0 0 14 14"><circle cx="7" cy="7" r="7" fill="#232a4a"/><path d="M4 7.2l2 2 4-4" stroke="#fff" stroke-width="1.5" fill="none"/></svg>Do Better Deals</li>
    <li><svg width="13" height="13" viewBox="0 0 14 14"><circle cx="7" cy="7" r="7" fill="#232a4a"/><path d="M4 7.2l2 2 4-4" stroke="#fff" stroke-width="1.5" fill="none"/></svg>Gain valuable skills</li>
    <li><svg width="13" height="13" viewBox="0 0 14 14"><circle cx="7" cy="7" r="7" fill="#232a4a"/><path d="M4 7.2l2 2 4-4" stroke="#fff" stroke-width="1.5" fill="none"/></svg>Advance your career</li>
    <li><svg width="13" height="13" viewBox="0 0 14 14"><circle cx="7" cy="7" r="7" fill="#232a4a"/><path d="M4 7.2l2 2 4-4" stroke="#fff" stroke-width="1.5" fill="none"/></svg>Counter vendor ploys</li>
    <li><svg width="13" height="13" viewBox="0 0 14 14"><circle cx="7" cy="7" r="7" fill="#232a4a"/><path d="M4 7.2l2 2 4-4" stroke="#fff" stroke-width="1.5" fill="none"/></svg>Save time, money and aggravation</li>
    <li><svg width="13" height="13" viewBox="0 0 14 14"><circle cx="7" cy="7" r="7" fill="#232a4a"/><path d="M4 7.2l2 2 4-4" stroke="#fff" stroke-width="1.5" fill="none"/></svg>Interact with your peers about vendors</li>
    <li><svg width="13" height="13" viewBox="0 0 14 14"><circle cx="7" cy="7" r="7" fill="#232a4a"/><path d="M4 7.2l2 2 4-4" stroke="#fff" stroke-width="1.5" fill="none"/></svg>Share working solutions to real situations</li>
  </ul>
  <div class="abs dots" style="left:519px;top:1565px;width:118px;height:118px" role="img" aria-label="Dot grid decoration"></div>
  <div class="abs photo" style="left:578px;top:1600px;width:470px;height:472px;border-radius:8px;background:linear-gradient(135deg,#e9e6e1,#b8a89a 60%,#4a3a30)" role="img" aria-label="Professional on a phone call taking notes at a desk"></div>
</section>

<section class="plans">
  <div class="abs rule" style="left:586px;top:2170px;width:29px"></div>
  <h2 class="abs sec-title" style="top:2191px">Flexible Plans</h2>
  <p class="abs" style="left:0;width:1200px;top:2226px;text-align:center;font-size:11px;font-weight:300;color:var(--muted)">Choose a plan that suits your needs</p>

  <div class="abs plan" style="left:151px;top:2285px;width:293px;height:390px">
    <h3>Free</h3>
    <div class="price">$0<small>/Month</small></div>
    <p class="plan-sub">For Small Business</p>
    <ul class="features">
      <li><svg width="12" height="12" viewBox="0 0 14 14"><circle cx="7" cy="7" r="7" fill="#0293ce"/><path d="M4 7.2l2 2 4-4" stroke="#fff" stroke-width="1.5" fill="none"/></svg>Vivamus curabitur</li>
      <li><svg width="12" height="12" viewBox="0 0 14 14"><circle cx="7" cy="7" r="7" fill="#0293ce"/><path d="M4 7.2l2 2 4-4" stroke="#fff" stroke-width="1.5" fill="none"/></svg>Dictum elit porttitor</li>
      <li><svg width="12" height="12" viewBox="0 0 14 14"><circle cx="7" cy="7" r="7" fill="#0293ce"/><path d="M4 7.2l2 2 4-4" stroke="#fff" stroke-width="1.5" fill="none"/></svg>Urna porta</li>
      <li><svg width="12" height="12" viewBox="0 0 14 14"><circle cx="7" cy="7" r="7" fill="#0293ce"/><path d="M4 7.2l2 2 4-4" stroke="#fff" stroke-width="1.5" fill="none"/></svg>Elit ornare</li>
    </ul>
    <div class="plan-btn">Choose Plan</div>
  </div>

  <div class="abs plan" style="left:454px;top:2285px;width:291px;height:390px">
    <h3>Standard</h3>
    <div class="price">$20<small>/Month</small></div>
    <p class="plan-sub">For Medium Size Business</p>
    <ul class="features">
      <li><svg width="12" height="12" viewBox="0 0 14 14"><circle cx="7" cy="7" r="7" fill="#0293ce"/><path d="M4 7.2l2 2 4-4" stroke="#fff" stroke-width="1.5" fill="none"/></svg>Vel praesent</li>
      <li><svg width="12" height="12" viewBox="0 0 14 14"><circle cx="7" cy="7" r="7" fill="#0293ce"/><path d="M4 7.2l2 2 4-4" stroke="#fff" stroke-width="1.5" fill="none"/></svg>Vehicula lobortis aliquam</li>
      <li><svg width="12" height="12" viewBox="0 0 14 14"><circle cx="7" cy="7" r="7" fill="#0293ce"/><path d="M4 7.2l2 2 4-4" stroke="#fff" stroke-width="1.5" fill="none"/></svg>Lectus nulla nunc</li>
      <li><svg width="12" height="12" viewBox="0 0 14 14"><circle cx="7" cy="7" r="7" fill="#0293ce"/><path d="M4 7.2l2 2 4-4" stroke="#fff" stroke-width="1.5" fill="none"/></svg>Non dapibus</li>
    </ul>
    <div class="plan-btn solid">Choose Plan</div>
  </div>

  <div class="abs plan" style="left:756px;top:2285px;width:292px;height:390px">
    <h3>Plus</h3>
    <div class="price">$45<small>/Month</small></div>
    <p class="plan-sub">For Large Size Companies</p>
    <ul class="features">
      <li><svg width="12" height="12" viewBox="0 0 14 14"><circle cx="7" cy="7" r="7" fill="#0293ce"/><path d="M4 7.2l2 2 4-4" stroke="#fff" stroke-width="1.5" fill="none"/></svg>Posuere condimentum vestibulum</li>
      <li><svg width="12" height="12" viewBox="0 0 14 14"><circle cx="7" cy="7" r="7" fill="#0293ce"/><path d="M4 7.2l2 2 4-4" stroke="#fff" stroke-width="1.5" fill="none"/></svg>Aliquam urna bibendum</li>
      <li><svg width="12" height="12" viewBox="0 0 14 14"><circle cx="7" cy="7" r="7" fill="#0293ce"/><path d="M4 7.2l2 2 4-4" stroke="#fff" stroke-width="1.5" fill="none"/></svg>Elit orci vivamus</li>
      <li><svg width="12" height="12" viewBox="0 0 14 14"><circle cx="7" cy="7" r="7" fill="#0293ce"/><path d="M4 7.2l2 2 4-4" stroke="#fff" stroke-width="1.5" fill="none"/></svg>Sed amet velit</li>
    </ul>
    <div class="plan-btn">Choose Plan</div>
  </div>
</section>

<footer>
  <div class="abs" style="left:151px;top:2799px;width:897px;height:1px;background:var(--rule)"></div>
  <div class="abs foot-col" style="left:151px;top:2840px">
    <h4>Learn about BRIVOL</h4>
    <p>Home<br>Join BRIVOL<br>Tour BRIVOL<br>Announcements</p>
  </div>
  <div class="abs foot-col" style="left:386px;top:2840px">
    <h4>Attend an Event</h4>
    <p>Tech Sourcing Forum<br>Events &amp; Workshops<br>Online Seminars<br>Regional Workshops</p>
  </div>
  <div class="abs foot-col" style="left:600px;top:2840px">
    <h4>Connect with BRIVOL</h4>
    <p>Get the Conference App<br>Contact Us<br>Chirpline<br>Friendspace</p>
  </div>
  <div class="abs foot-col" style="left:844px;top:2840px">
    <h4>Contact Us</h4>
    <p>+1.555.010.4400</p>
    <p style="margin-top:8px">BRIVOL - The Guild of Tech Sourcing<br>Specialists and Buyers<br>Drawer 4180<br>Lakemont, FL 30000-0000</p>
  </div>

  <div class="abs bottom-bar">
    <span class="social" style="left:151px;font-size:9.5px">BRIVOL ©2020</span>
    <span class="social" style="left:892px">Friendspace</span>
    <span class="social" style="left:955px">Chirpline</span>
    <span class="social" style="left:1010px">Linkora</span>
  </div>
</footer>

</body>
</html>
```